New Company Business Card design

Looking for a corporate looking business card utilising my new logo design - the logo i would like embossed as one option and flat as another - simplistic but stylish - less is more - we are an import export business launching into the market - i would like a couple of options as main background - Grey or Black

```html
<!DOCTYPE html>
<html lang="en">
<head>
<meta charset="utf-8">
<title>Meridian Trade Partners – Business Card</title>
<link href="https://fonts.googleapis.com/css2?family=Cinzel:wght@500&family=Lato:wght@300;400&display=swap" rel="stylesheet">
<style>
  :root {
    --stage: #2a2a2c;
    --card: #17181b;
    --card-edge: #0e0f11;
    --emboss: #24262a;
    --blue: #2a7fd0;
    --blue-deep: #1b5fa6;
    --text-light: #f2f2f2;
    --text-muted: #9a9ca0;
  }
  * { box-sizing: border-box; margin: 0; padding: 0; }
  html, body { width: 1200px; height: 1200px; overflow: hidden; }
  body {
    background: var(--stage);
    font-family: "Lato", sans-serif;
    display: flex;
    flex-direction: column;
    align-items: center;
    justify-content: center;
    gap: 60px;
  }
  .card {
    position: relative;
    width: 900px;
    height: 514px;
    background: var(--card);
    box-shadow: 0 18px 40px rgba(0,0,0,.55);
    border: 1px solid var(--card-edge);
  }
  .wordmark {
    position: absolute;
    display: flex;
    align-items: center;
    gap: 18px;
    font-family: "Cinzel", serif;
    font-weight: 500;
    letter-spacing: 2px;
    line-height: 1.15;
  }
  .wordmark-dot {
    width: 46px; height: 46px;
    border-radius: 50%;
    flex: none;
  }
  .card-back .wordmark {
    left: 50%; top: 50%;
    transform: translate(-50%, -50%);
    font-size: 34px;
    color: var(--emboss);
  }
  .card-back .wordmark-dot { background: var(--emboss); }
  .card-front .wordmark {
    left: 80px; top: 300px;
    font-size: 30px;
    color: var(--blue);
  }
  .card-front .wordmark-dot { background: var(--blue); }
  .divider {
    position: absolute;
    left: 520px; top: 150px;
    width: 2px; height: 230px;
    background: linear-gradient(to bottom, transparent, var(--blue) 45%, transparent);
  }
  .contact {
    position: absolute;
    left: 575px; top: 110px;
    color: var(--text-light);
  }
  .contact-name { font-size: 36px; font-weight: 400; }
  .contact-role { font-size: 20px; font-weight: 300; color: var(--text-muted); margin-top: 2px; }
  .contact-list { list-style: none; margin-top: 36px; }
  .contact-list li {
    display: flex; align-items: center; gap: 16px;
    font-size: 20px; margin-bottom: 9px;
  }
  .contact-list li.address { font-size: 16px; line-height: 1.3; margin-bottom: 20px; }
  .contact-list svg { width: 20px; height: 20px; flex: none; fill: none; stroke: var(--blue); stroke-width: 1.8; }
  .contact-list svg.solid { fill: var(--blue); stroke: none; }
</style>
</head>
<body>
  <section class="card card-back">
    <div class="wordmark"><span class="wordmark-dot"></span><span>Meridian<br>Trade Partners</span></div>
  </section>

  <section class="card card-front">
    <div class="wordmark"><span class="wordmark-dot"></span><span>Meridian<br>Trade Partners</span></div>
    <div class="divider"></div>
    <div class="contact">
      <p class="contact-name">Daniel Hartley</p>
      <p class="contact-role">Director</p>
      <ul class="contact-list">
        <li class="address">
          <svg class="solid" viewBox="0 0 24 24"><path d="M12 2a7 7 0 0 0-7 7c0 5 7 13 7 13s7-8 7-13a7 7 0 0 0-7-7zm0 9.5A2.5 2.5 0 1 1 12 6.5a2.5 2.5 0 0 1 0 5z"/></svg>
          <span>Street adress, loremp ipsum<br>Your city, 1568</span>
        </li>
        <li>
          <svg class="solid" viewBox="0 0 24 24"><path d="M6.6 10.8a15 15 0 0 0 6.6 6.6l2.2-2.2a1 1 0 0 1 1-.25 11 11 0 0 0 3.6.6 1 1 0 0 1 1 1V20a1 1 0 0 1-1 1A17 17 0 0 1 3 4a1 1 0 0 1 1-1h3.5a1 1 0 0 1 1 1c0 1.25.2 2.45.6 3.6a1 1 0 0 1-.25 1z"/></svg>
          <span>123 456 7890</span>
        </li>
        <li>
          <svg viewBox="0 0 24 24"><rect x="7" y="2" width="10" height="20" rx="2"/><line x1="11" y1="18" x2="13" y2="18"/></svg>
          <span>001 235 4589</span>
        </li>
        <li>
          <svg viewBox="0 0 24 24"><rect x="4" y="9" width="16" height="10" rx="1"/><rect x="7" y="3" width="10" height="6"/><line x1="8" y1="14" x2="16" y2="14"/></svg>
          <span>123 456 7898</span>
        </li>
        <li>
          <svg viewBox="0 0 24 24"><circle cx="12" cy="12" r="9"/><path d="M3 12h18M12 3c3 3 3 15 0 18M12 3c-3 3-3 15 0 18"/></svg>
          <span>yourwebsitename.com</span>
        </li>
        <li>
          <svg viewBox="0 0 24 24"><rect x="3" y="6" width="18" height="12"/><path d="M3 6l9 7 9-7"/></svg>
          <span>yourname@emal.com</span>
        </li>
      </ul>
    </div>
  </section>
</body>
</html>
```